the halvorsen group premier division

design a DL A4 tri fold brochure to reflect our creative landscape business
my web site www.thehalvorsengroup.com.au
has all the information needed
i will also be updating the website to be more updated and creative design

```html
<!DOCTYPE html>
<html lang="en">
<head>
<meta charset="utf-8">
<title>The Halvorsen Group – Tri-fold Brochure</title>
<link href="https://fonts.googleapis.com/css2?family=Ubuntu:wght@400;500;700&family=Oswald:wght@400&display=swap" rel="stylesheet">
<style>
:root{
  --green:#6cbf3a;
  --green-dark:#4e9e25;
  --green-light:#8fd056;
  --orange:#f08a12;
  --ink:#222;
  --grey-text:#4a4a4a;
  --paper:#f4f4f4;
  --bg:#e6e6e4;
}
*{box-sizing:border-box;margin:0;padding:0}
html,body{width:878px;height:1200px;overflow:hidden;background:var(--bg)}
body{font-family:'Ubuntu',sans-serif;color:var(--grey-text);position:relative}
.sheet{position:absolute;left:16px;width:846px;height:572px;background:var(--paper);box-shadow:0 2px 8px rgba(0,0,0,.25);overflow:hidden}
.sheet--outside{top:18px}
.sheet--inside{top:610px}
.panel{position:absolute;top:0;height:100%;width:282px;overflow:hidden}
.panel--1{left:0}.panel--2{left:282px}.panel--3{left:564px}
.photo{position:absolute;left:0;width:100%}
.curve{position:absolute;left:0;width:100%}
.grad-paper{background:linear-gradient(180deg,#fff 0%,#ededed 100%)}
.green-panel{background:linear-gradient(160deg,var(--green-light) 0%,var(--green) 45%,var(--green-dark) 100%);color:#fff}

/* wordmark: one colour, one weight, one plain circle */
.wordmark{display:flex;align-items:center;justify-content:center;gap:7px}
.wordmark-dot{width:11px;height:11px;border-radius:50%;background:currentColor;flex:none}
.wordmark-name{font-weight:700;font-size:20px;letter-spacing:-.3px;white-space:nowrap}

h2.services-title{position:absolute;left:16px;top:279px;font-size:12px;font-weight:500;color:var(--ink)}
.intro{position:absolute;left:16px;right:16px;font-size:9.5px;line-height:1.38;color:#555;text-align:justify}
.service-list{position:absolute;left:14px;top:392px;right:10px;list-style:none}
.service-list li{display:flex;gap:8px;margin-bottom:10px;align-items:flex-start}
.svc-icon{flex:none;width:34px;height:34px;border-radius:50%;background:var(--green);border:3px solid #dcdcdc;display:flex;align-items:center;justify-content:center}
.svc-name{font-size:10px;color:var(--ink);text-transform:uppercase;margin-top:2px}
.svc-desc{font-size:7.4px;line-height:1.3;color:#666}

.offer-list{position:absolute;top:212px;left:0;right:0;list-style:none;text-align:center;font-size:10px;line-height:20px}
.contact-pill{position:absolute;top:350px;left:40px;right:40px;height:24px;border-radius:12px;background:linear-gradient(#6a6a6a,#4a4a4a);color:#fff;font-size:12px;text-align:center;line-height:24px;box-shadow:0 2px 4px rgba(0,0,0,.3)}
.contact{position:absolute;left:0;right:0;text-align:center;font-size:12.5px}
.socials{position:absolute;top:518px;left:0;right:0;display:flex;justify-content:center;gap:14px}
.socials span{width:22px;height:22px;border-radius:50%;border:1.5px solid #fff}

.headline{font-family:'Oswald',sans-serif;font-weight:400;color:var(--green);font-size:16px;text-align:center;text-transform:uppercase}
.tagline{font-size:11px;text-align:center}
.call-pill{position:absolute;left:33px;right:17px;height:24px;border-radius:12px;background:linear-gradient(#666,#484848);color:#fff;font-family:'Oswald',sans-serif;font-size:15px;display:flex;align-items:center;justify-content:center;gap:6px}
.phone-ico{width:13px;height:13px}
.web{position:absolute;left:16px;right:0;text-align:center;font-size:10px;color:#333}

.about{position:absolute;left:16px;right:16px;top:42px}
.about .headline{color:#fff;font-size:16.5px}
.about .tagline{color:#fff;margin:4px 0 14px}
.about p{font-size:9.6px;line-height:1.38;margin-bottom:10px;text-align:justify}

.spread{position:absolute;left:282px;top:0;width:564px;height:100%}
.round-photo{position:absolute;border-radius:50%;border:4px solid #fff;box-shadow:0 2px 5px rgba(0,0,0,.3)}
.cat{position:absolute;left:22px;width:250px}
.cat-head{display:flex;align-items:center;gap:10px;font-size:12px;color:var(--ink);margin-bottom:7px}
.cat ul{list-style:none}
.cat li{font-size:9.6px;color:#444;margin-bottom:5px;display:flex;align-items:center;gap:8px;padding-left:4px}
.tick{width:9px;height:9px;flex:none}
.process{position:absolute;left:292px;top:250px;width:256px}
.process h3{font-size:11.5px;font-weight:400;color:var(--ink);margin-bottom:8px}
.step{display:flex;gap:8px;font-size:9.6px;line-height:1.35;color:#555;padding:6px 0 8px;border-bottom:1px solid #cfcfcf;text-align:justify}
.step:last-child{border-bottom:none}
.step .tick{width:11px;height:11px;margin-top:1px}
.swoosh-brand{position:absolute;right:12px;bottom:40px;color:#fff}
.swoosh-brand .wordmark-name{font-size:17px}
.swoosh-call{position:absolute;right:12px;bottom:8px;color:#fff;font-family:'Oswald',sans-serif;font-size:15px;display:flex;align-items:center;gap:5px}
</style>
</head>
<body>

<section class="sheet sheet--outside">
  <div class="panel panel--1 grad-paper">
    <div class="photo" style="top:0;height:240px;background:linear-gradient(180deg,#1f3a66 0%,#6a7e98 45%,#2a77c0 75%,#1a5fa6 100%)" role="img" aria-label="Luxury two-storey home at dusk with illuminated swimming pool"></div>
    <svg class="curve" style="top:210px" width="282" height="60" viewBox="0 0 282 60" preserveAspectRatio="none">
      <path d="M0 30 Q140 0 282 10 L282 60 L0 60Z" fill="var(--orange)"/>
      <path d="M0 42 Q140 12 282 20 L282 60 L0 60Z" fill="#fff"/>
    </svg>
    <h2 class="services-title">OUR SERVICES</h2>
    <p class="intro" style="top:302px">As a full service landscape and construction business, we can ensure our client’s outdoor vision comes to fruition from concept to completion.</p>
    <p class="intro" style="top:355px">The Halvorsen Group proudly offers high-end landscaping in residential and acreage environments.</p>
    <ul class="service-list">
      <li><span class="svc-icon"><svg width="16" height="16" viewBox="0 0 16 16"><path d="M3 3L13 13M13 3L3 13" stroke="#fff" stroke-width="2.4" stroke-linecap="round"/></svg></span>
        <div><div class="svc-name">Consultation and Design</div><div class="svc-desc">We will meet you for a full landscape design concept to discuss an existing plan.</div></div></li>
      <li><span class="svc-icon"><svg width="16" height="16" viewBox="0 0 16 16"><path d="M8 15V7M8 8Q3 8 3 3Q8 3 8 8M8 7Q13 7 13 2Q8 2 8 7" fill="#fff"/><path d="M3 15H13" stroke="#fff" stroke-width="1.5"/></svg></span>
        <div><div class="svc-name">Earthwork &amp; Site Preparation</div><div class="svc-desc">Depending on the nature of your foundation, earth need be prepared for construction and planting.</div></div></li>
      <li><span class="svc-icon"><svg width="16" height="16" viewBox="0 0 16 16"><circle cx="8" cy="5" r="3" fill="#fff"/><path d="M2 15Q2 9 8 9Q14 9 14 15Z" fill="#fff"/></svg></span>
        <div><div class="svc-name">Installation &amp; Construction</div><div class="svc-desc">The Halvorsen group are a professional company that works with a whole range of structural designs.</div></div></li>
      <li><span class="svc-icon"><svg width="16" height="16" viewBox="0 0 16 16"><path d="M3 13L11 5M5 3L13 11" stroke="#fff" stroke-width="2.2" stroke-linecap="round"/></svg></span>
        <div><div class="svc-name">Maintenance Programs</div><div class="svc-desc">We understand people can be ‘caught up’ or procrastinate in attending to landscape maintenance.</div></div></li>
    </ul>
  </div>

  <div class="panel panel--2 green-panel">
    <div class="wordmark" style="position:absolute;top:160px;left:0;right:0;color:#fff">
      <span class="wordmark-dot"></span><span class="wordmark-name">The Halvorsen Group</span>
    </div>
    <ul class="offer-list">
      <li>Creative landscape garden design and construction</li>
      <li>Limited acces track bobcat &amp; excavator</li>
      <li>Water Features and Bespoke Plant Design</li>
      <li>Concreting, Paving and Gravel Driveways</li>
      <li>Decking, Feature Walls, Screens and Retaining</li>
      <li>Wall Solutions</li>
    </ul>
    <div class="contact-pill">CONTACT US:</div>
    <div class="contact" style="top:394px">PO Box 742, Brookvale 3094</div>
    <div class="contact" style="top:430px">0412 38 64 90</div>
    <div class="contact" style="top:465px;line-height:18px">rob@thehalvorsengroup.com.au<br>www.thehalvorsengroup.com.au</div>
    <div class="socials"><span></span><span></span><span></span></div>
  </div>

  <div class="panel panel--3 grad-paper">
    <div class="photo" style="top:0;height:400px;background:linear-gradient(180deg,#dfe6e8 0%,#5d7a4a 30%,#3c4a3a 55%,#7b7b78 80%,#5f5f5c 100%)" role="img" aria-label="Garden courtyard with grey outdoor lounge and lush planting"></div>
    <svg class="curve" style="top:350px" width="282" height="80" viewBox="0 0 282 80" preserveAspectRatio="none">
      <path d="M0 38 Q150 44 282 0 L282 80 L0 80Z" fill="var(--orange)"/>
      <path d="M0 50 Q150 56 282 14 L282 80 L0 80Z" fill="#fff"/>
    </svg>
    <div class="wordmark" style="position:absolute;top:432px;left:0;right:0;color:var(--ink)">
      <span class="wordmark-dot"></span><span class="wordmark-name">The Halvorsen Group</span>
    </div>
    <div class="headline" style="position:absolute;top:484px;left:16px;right:0">Landscape Consulting and Design</div>
    <div class="tagline" style="position:absolute;top:506px;left:16px;right:0;color:#333">Landscaping to your Lifestyle</div>
    <div class="call-pill" style="top:526px"><span>CALL US TODAY</span>
      <svg class="phone-ico" viewBox="0 0 14 14"><circle cx="7" cy="7" r="6" fill="none" stroke="#fff"/><path d="M5 4L6 6L5.4 6.8Q6.4 8.4 7.6 8.6L8.2 8L10 9L9.4 10.2Q6.6 10.4 4.2 6.4Q3.8 4.4 5 4Z" fill="#fff"/></svg>
      <span>0412 38 64 90</span></div>
    <div class="web" style="top:554px">www.thehalvorsengroup.com.au</div>
  </div>
</section>

<section class="sheet sheet--inside">
  <div class="panel panel--1 green-panel">
    <div class="about">
      <div class="headline">Landscape Consulting and Design</div>
      <div class="tagline">Landscaping to your Lifestyle</div>
      <p>Rob Ellery, head of The Halvorsen Group, offers a team that dedicates their efforts from concept development to installation and maintenance to ensure the outdoor creation becomes part of the client’s home and life experience with visual, tactile and sensory inclusions.</p>
      <p>Over its 20years, the business has developed a strong reputation for positive customer experiences, innovative designs and quality outcomes to suit individual needs and design styles.</p>
      <p>The Halvorsen Group is a full-service landscaping and construction team that relish the journey to deliver high-end and bespoke outdoor designs.</p>
    </div>
    <div class="photo" style="top:325px;height:247px;background:linear-gradient(180deg,#cfd6de 0%,#8d949c 35%,#6a4a2e 65%,#2f4a25 100%)" role="img" aria-label="Grand home entrance with timber double doors and garden hedges"></div>
    <svg class="curve" style="top:310px" width="282" height="40" viewBox="0 0 282 40" preserveAspectRatio="none">
      <path d="M0 0 L282 0 L282 8 Q140 6 0 34Z" fill="var(--green-dark)"/>
      <path d="M0 34 Q140 6 282 8 L282 18 Q140 14 0 40Z" fill="var(--orange)"/>
    </svg>
  </div>

  <div class="spread grad-paper">
    <div class="photo" style="top:0;height:200px;background:linear-gradient(90deg,#2e3a2c 0%,#7f7a6c 30%,#3f4a3c 55%,#5c4a3e 80%,#2b2b2b 100%)" role="img" aria-label="Outdoor courtyard with sandstone planter, timber bench and chairs"></div>
    <svg class="curve" style="top:150px" width="564" height="90" viewBox="0 0 564 90" preserveAspectRatio="none">
      <path d="M0 40 Q280 70 564 10 L564 90 L0 90Z" fill="var(--orange)"/>
      <path d="M0 52 Q280 82 564 24 L564 90 L0 90Z" fill="#fff"/>
    </svg>
    <div class="round-photo" style="left:314px;top:116px;width:110px;height:110px;background:linear-gradient(180deg,#8a6e4e 0%,#6fb2a8 60%,#3b8d86 100%)" role="img" aria-label="Plunge pool with timber screening"></div>
    <div class="round-photo" style="left:432px;top:116px;width:110px;height:110px;background:linear-gradient(180deg,#3c6a32 0%,#a33a36 50%,#4d7a3e 100%)" role="img" aria-label="Garden pathway leading to a red door"></div>

    <div class="cat" style="top:256px">
      <div class="cat-head"><svg width="28" height="28" viewBox="0 0 28 28"><circle cx="13" cy="9" r="6" fill="var(--green)"/><path d="M3 27Q3 16 13 16Q23 16 23 27Z" fill="var(--green)"/></svg>CONSTRUCTION</div>
      <ul>
        <li><svg class="tick" viewBox="0 0 10 10"><circle cx="5" cy="5" r="4.3" fill="none" stroke="var(--green)"/><path d="M3 5L4.5 6.5L7 3.8" fill="none" stroke="var(--green)"/></svg>Bespoke Structural Features</li>
        <li><svg class="tick" viewBox="0 0 10 10"><circle cx="5" cy="5" r="4.3" fill="none" stroke="var(--green)"/><path d="M3 5L4.5 6.5L7 3.8" fill="none" stroke="var(--green)"/></svg>Water Features</li>
        <li><svg class="tick" viewBox="0 0 10 10"><circle cx="5" cy="5" r="4.3" fill="none" stroke="var(--green)"/><path d="M3 5L4.5 6.5L7 3.8" fill="none" stroke="var(--green)"/></svg>Paving &amp; Pathways</li>
        <li><svg class="tick" viewBox="0 0 10 10"><circle cx="5" cy="5" r="4.3" fill="none" stroke="var(--green)"/><path d="M3 5L4.5 6.5L7 3.8" fill="none" stroke="var(--green)"/></svg>Concreting and Aggregate</li>
      </ul>
    </div>
    <div class="cat" style="top:382px">
      <div class="cat-head"><svg width="28" height="28" viewBox="0 0 28 28"><circle cx="10" cy="9" r="7" fill="var(--green)"/><circle cx="19" cy="14" r="6" fill="var(--green)"/><rect x="12" y="17" width="3" height="10" fill="var(--green)"/></svg>GARDEN</div>
      <ul>
        <li><svg class="tick" viewBox="0 0 10 10"><circle cx="5" cy="5" r="4.3" fill="none" stroke="var(--green)"/><path d="M3 5L4.5 6.5L7 3.8" fill="none" stroke="var(--green)"/></svg>Plant &amp; Tree supply &amp; installation</li>
        <li><svg class="tick" viewBox="0 0 10 10"><circle cx="5" cy="5" r="4.3" fill="none" stroke="var(--green)"/><path d="M3 5L4.5 6.5L7 3.8" fill="none" stroke="var(--green)"/></svg>Earth Preparation</li>
        <li><svg class="tick" viewBox="0 0 10 10"><circle cx="5" cy="5" r="4.3" fill="none" stroke="var(--green)"/><path d="M3 5L4.5 6.5L7 3.8" fill="none" stroke="var(--green)"/></svg>Lawns</li>
        <li><svg class="tick" viewBox="0 0 10 10"><circle cx="5" cy="5" r="4.3" fill="none" stroke="var(--green)"/><path d="M3 5L4.5 6.5L7 3.8" fill="none" stroke="var(--green)"/></svg>Irrigation Systems</li>
      </ul>
    </div>
    <div class="cat" style="top:510px">
      <div class="cat-head"><svg width="28" height="28" viewBox="0 0 28 28"><path d="M3 12H22L18 22H7Z" fill="var(--green)"/><circle cx="10" cy="25" r="2.5" fill="var(--green)"/><path d="M13 12V4M13 6Q8 6 8 2M13 6Q18 6 18 2" stroke="var(--green)" stroke-width="2" fill="none"/></svg>MAINTENANCE</div>
      <ul>
        <li><svg class="tick" viewBox="0 0 10 10"><circle cx="5" cy="5" r="4.3" fill="none" stroke="var(--green)"/><path d="M3 5L4.5 6.5L7 3.8" fill="none" stroke="var(--green)"/></svg>Garden &amp; Structural</li>
      </ul>
    </div>

    <div class="process">
      <h3>THE PROCESS</h3>
      <div class="step"><svg class="tick" viewBox="0 0 10 10"><circle cx="5" cy="5" r="4.3" fill="none" stroke="var(--green)"/><path d="M3 5L4.5 6.5L7 3.8" fill="none" stroke="var(--green)"/></svg><span>THG can work with an existing design or create a landscape design to suit your needs.</span></div>
      <div class="step"><svg class="tick" viewBox="0 0 10 10"><circle cx="5" cy="5" r="4.3" fill="none" stroke="var(--green)"/><path d="M3 5L4.5 6.5L7 3.8" fill="none" stroke="var(--green)"/></svg><span>Once a design has been established, Rob Ellery will go over your plans onsite and discuss the requirements to suit your space and climate and provide advice as needed.</span></div>
      <div class="step"><svg class="tick" viewBox="0 0 10 10"><circle cx="5" cy="5" r="4.3" fill="none" stroke="var(--green)"/><path d="M3 5L4.5 6.5L7 3.8" fill="none" stroke="var(--green)"/></svg><span>Rob will project-manage your entire outdoor construction and ensure you are updated throughout the journey.</span></div>
      <div class="step"><svg class="tick" viewBox="0 0 10 10"><circle cx="5" cy="5" r="4.3" fill="none" stroke="var(--green)"/><path d="M3 5L4.5 6.5L7 3.8" fill="none" stroke="var(--green)"/></svg><span>Our clients will experience honesty, integrity, and professionalism throughout the project which allows them to embrace their outdoor living after completion.</span></div>
    </div>

    <svg class="curve" style="bottom:0" width="564" height="90" viewBox="0 0 564 90" preserveAspectRatio="none">
      <path d="M250 90 Q330 20 564 6 L564 90Z" fill="#bdbdbd"/>
      <path d="M256 90 Q336 26 564 14 L564 90Z" fill="var(--green)"/>
    </svg>
    <div class="swoosh-brand">
      <div class="wordmark"><span class="wordmark-dot" style="width:9px;height:9px"></span><span class="wordmark-name">The Halvorsen Group</span></div>
    </div>
    <div class="swoosh-call"><span>CALL US TODAY</span>
      <svg class="phone-ico" viewBox="0 0 14 14"><circle cx="7" cy="7" r="6" fill="none" stroke="#fff"/><path d="M5 4L6 6L5.4 6.8Q6.4 8.4 7.6 8.6L8.2 8L10 9L9.4 10.2Q6.6 10.4 4.2 6.4Q3.8 4.4 5 4Z" fill="#fff"/></svg>
      <span>0412 38 64 90</span></div>
  </div>
</section>

</body>
</html>
```